Vehicles Brochure Diagram

Task Outline
Create diagrams for our new vehicles brochures

Task Description

Who are we:
KTW is New Zealand's largest Business Group Buying organisation, helping organisations nationwide reduce their running costs. We offer members the best deals from over 100 Contracted Suppliers, anything from vehicles, stationery to electronics and coffee.

The project:
We need 2 diagrams to illustrate the benefits of our vehicle services. The diagram will be used in our brochures (example attached)

1. A Diagram illustrating/explaining the elements that are involved in purchasing a new car & how our service ties it all together to provide the best solution.
- Please see the Diagram 1 PDF for a rough wireframe of the elements involved

2. Another small diagram inserted on an separate page to demonstrate how our services can increase safety & profit and reduce costs & risks (PDF: Diagram 2 Details)

The design needs to be clean, clear and simple that it’s easy to understand within a few seconds of looking at it. Feel free to explore with different elements in the realm of infographics, flowcharts & diagrams to best communicate the idea visually.
Updates

Just thought I’ll share some of the feedback we’re giving tosubmissions that have been coming through to help with new submissions

-Challenge & be creative about the ways you demonstratethe elements

-We don’t want to see your design replicating the ones that isdrawn. The purpose of it is only to provide you with the content in context

-We can’t emphasis enough that the style pdf is only areference and not the look you should imitate. 

If you have any question please feel free to contact me.Looking forward to see your designs!

Project Deadline Extended
Reason: We're keen to see more approaches & creative ways of interpreting the content rather than a standard cycle diagram. Entries so far have been good but quite literal, we will provide feedback to help steer it in the right direction.

Target Market(s)

Business professionals, Decision makers on a corporate level & prospects.

Industry/Entity Type

Electronics

Requirements
Must have

• Likes – simple, clean & clear, uncluttered

Dislikes – Overcrowded images, text, & colours. Overly expressive typeface. Please no literal illustration of our sketches or colored version of our sketch.

Font: -Myriad Pro

Colour: Please refer to the color palette in the ‘Diagram Color & Style’ PDF

The brochures are attached with content to provide context that might inform the design better,

Dimensions & the amount of space you have to work with will also be highlighted

```html
<!DOCTYPE html>
<html lang="en">
<head>
<meta charset="UTF-8">
<title>Vehicle Services Benefits</title>
<link rel="stylesheet" href="https://fonts.googleapis.com/css2?family=Source+Sans+3:wght@400;600&display=swap">
<style>
  :root {
    --page-bg: #ffffff;
    --ink: #231f20;
    --orange-light: #f5b060;
    --orange: #f39a1f;
    --orange-deep: #ee8a12;
    --green-deep: #3fa23a;
    --green: #5cb84e;
    --green-light: #8fcf78;
    --icon-white: #ffffff;
  }
  html, body {
    margin: 0;
    padding: 0;
    width: 1200px;
    height: 900px;
    overflow: hidden;
    background: var(--page-bg);
  }
  .canvas {
    position: relative;
    width: 1200px;
    height: 900px;
    font-family: "Source Sans 3", "Myriad Pro", Arial, sans-serif;
    color: var(--ink);
  }
  .arrow-graphic {
    position: absolute;
    top: 0;
    left: 0;
    width: 1200px;
    height: 900px;
  }
  .benefit-column {
    position: absolute;
    top: 432px;
  }
  .benefit-column--increase { left: 291px; }
  .benefit-column--reduce { left: 711px; }
  .benefit-heading {
    margin: 0 0 14px 0;
    font-size: 30px;
    font-weight: 600;
    line-height: 1.2;
    letter-spacing: -0.2px;
  }
  .benefit-list {
    list-style: none;
    margin: 0;
    padding: 0;
  }
  .benefit-list li {
    position: relative;
    padding-left: 26px;
    font-size: 21.5px;
    line-height: 32px;
  }
  .benefit-list li::before {
    content: "";
    position: absolute;
    left: 9px;
    top: 14px;
    width: 5px;
    height: 5px;
    border-radius: 50%;
    background: var(--ink);
  }
</style>
</head>
<body>
<div class="canvas">
  <svg class="arrow-graphic" viewBox="0 0 1200 900" xmlns="http://www.w3.org/2000/svg">
    <defs>
      <linearGradient id="increaseFill" x1="0" y1="0" x2="1" y2="1">
        <stop offset="0" stop-color="var(--orange-light)"/>
        <stop offset="0.55" stop-color="var(--orange)"/>
        <stop offset="1" stop-color="var(--orange-deep)"/>
      </linearGradient>
      <linearGradient id="reduceFill" x1="0" y1="0" x2="1" y2="1">
        <stop offset="0" stop-color="var(--green-deep)"/>
        <stop offset="0.5" stop-color="var(--green)"/>
        <stop offset="1" stop-color="var(--green-light)"/>
      </linearGradient>
    </defs>

    <!-- Increase arrow -->
    <g class="increase-arrow">
      <path d="M423 170 L593 275 Q596 278 590 278 L557 278 L557 362 Q557 371 548 371 L290 371 Q281 371 281 362 L281 278 L251 278 Q245 278 248 275 Z"
            fill="url(#increaseFill)"/>
      <g class="icon-health">
        <rect x="333" y="255" width="72" height="72" rx="9" fill="var(--icon-white)"/>
        <path d="M361 270 h16 v16 h16 v16 h-16 v16 h-16 v-16 h-16 v-16 h16 z" fill="var(--orange)"/>
      </g>
      <rect class="icon-presenter" x="430" y="252" width="96" height="80" rx="6"
            fill="var(--icon-white)" fill-opacity="0.35"
            role="img" aria-label="Pictogram of a presenter pointing at a rising chart"/>
    </g>

    <!-- Reduce arrow -->
    <g class="reduce-arrow">
      <path d="M697 188 L954 188 Q962 188 962 196 L962 270 L990 270 Q997 270 992 276 L832 370 Q825 374 818 370 L658 276 Q653 270 660 270 L689 270 L689 196 Q689 188 697 188 Z"
            fill="url(#reduceFill)"/>
      <g class="icon-fuel" fill="var(--icon-white)">
        <path d="M734 215 q0-7 7-7 h30 q7 0 7 7 v68 h4 v8 h-52 v-8 h4 z"/>
        <rect x="741" y="218" width="30" height="20" rx="2" fill="var(--green-deep)"/>
        <path d="M778 235 h6 q6 0 6 6 v30 q0 4 4 4 q4 0 4-4 v-32 l-7-9 4-3 8 10 v34 q0 10-9 10 q-10 0-10-10 v-30 q0-2-2-2 h-4 z"/>
      </g>
      <rect class="icon-plants" x="828" y="212" width="94" height="82" rx="6"
            fill="var(--icon-white)" fill-opacity="0.35"
            role="img" aria-label="Pictogram of two young leafy plants"/>
    </g>
  </svg>

  <section class="benefit-column benefit-column--increase">
    <h2 class="benefit-heading">Increase your</h2>
    <ul class="benefit-list">
      <li>Driver Safety</li>
      <li>Bottom Line Profit</li>
      <li>Capital spend</li>
      <li>Customer satisfaction</li>
      <li>Organisation Expectations</li>
    </ul>
  </section>

  <section class="benefit-column benefit-column--reduce">
    <h2 class="benefit-heading">Reduce your</h2>
    <ul class="benefit-list">
      <li>Carbon Footprints</li>
      <li>Business overheads</li>
      <li>Company risk</li>
      <li>Operational costs</li>
      <li>Speeding tickets</li>
    </ul>
  </section>
</div>
</body>
</html>
```